Innovative payment service needs cool business cards

Velto Payments makes it easy for customers to make purchases with their mobile phones. Our flagship service is called KirbeX (http://www.KirbeX.example). We need cards for the executive team.

Please use Lato (available from Plimsoll Web Type) for text and base the colour scheme off of the colours in the logos (attached).

The front of the card should have a smallish Velto logo and the following text, laid out however, and using whatever icons, you like:
http://www.veltopayments.example
Tomas Wrenfield
CEO
tomas@veltopayments.example
+ 62 817 402 36918
+ 65 9143 5820
+1 650 271 8845

The back of the card should have a largish Kirbe logo and the following text, again laid out however, and using whatever icons, you like:
http://www.KirbeX.example
@KirbeX_id
http://www.facebook.com/KirbeX

We will use ZEP for printing so please use one of their templates http://us.zepprint.example/help/faq/templates-and-guidelines.html.

```html
<!DOCTYPE html>
<html lang="en">
<head>
<meta charset="utf-8">
<title>KirbeX business cards</title>
<link rel="stylesheet" href="https://fonts.googleapis.com/css2?family=Montserrat:wght@700&family=Lato:wght@400;700&display=swap">
<style>
  :root {
    --navy: #17325a;
    --orange: #ec8a24;
    --white: #ffffff;
    --stage: #2e2e2e;
  }
  * { margin: 0; padding: 0; box-sizing: border-box; }
  html, body { width: 1200px; height: 900px; overflow: hidden; background: var(--stage); }
  .stage { position: relative; width: 1200px; height: 900px; }
  .card {
    position: absolute; left: 280px; width: 640px; height: 366px;
    background: var(--white); overflow: hidden;
  }
  .card--contact { top: 60px; }
  .card--brand { top: 474px; }
  .card__art { position: absolute; inset: 0; width: 100%; height: 100%; }

  /* contact side */
  .contact__logo {
    position: absolute; left: 40px; top: 150px;
    font-family: "Montserrat", sans-serif; font-weight: 700;
    font-size: 40px; color: var(--navy); letter-spacing: -0.5px;
  }
  .contact__person { position: absolute; right: 40px; top: 52px; text-align: right; }
  .contact__name {
    font-family: "Montserrat", sans-serif; font-weight: 700;
    font-size: 22px; color: var(--navy);
  }
  .contact__role {
    font-family: "Lato", sans-serif; font-size: 11px; color: var(--orange);
    letter-spacing: 0.5px; margin-top: 1px;
  }
  .contact__list {
    position: absolute; right: 36px; top: 136px; list-style: none;
    font-family: "Lato", sans-serif; font-size: 14px; color: var(--white);
    text-align: right; line-height: 23px;
  }
  .contact__list li { display: flex; justify-content: flex-end; align-items: center; gap: 8px; }
  .contact__list .is-strong { font-weight: 700; }
  .contact__icon { width: 13px; height: 13px; flex: none; }

  /* brand side */
  .brand__logo {
    position: absolute; left: 40px; top: 112px;
    font-family: "Montserrat", sans-serif; font-weight: 700;
    font-size: 132px; line-height: 1; color: var(--navy); letter-spacing: -3px;
  }
  .brand__url {
    position: absolute; left: 76px; top: 258px;
    font-family: "Lato", sans-serif; font-size: 22px; color: var(--orange); letter-spacing: 1.5px;
  }
  .brand__social {
    position: absolute; left: 44px; top: 318px; display: flex; gap: 48px;
    font-family: "Lato", sans-serif; font-size: 18px; color: var(--navy);
  }
  .brand__social span { display: flex; align-items: center; gap: 8px; }
  .brand__social i { width: 18px; height: 18px; background: var(--orange); border-radius: 3px; display: block; }
</style>
</head>
<body>
<main class="stage">

  <section class="card card--contact" aria-label="Contact side">
    <svg class="card__art" viewBox="0 0 640 366" aria-hidden="true">
      <polygon points="0,366 0,318 330,118 640,118 640,366" fill="var(--orange)"/>
    </svg>
    <div class="contact__logo">KirbeX</div>
    <div class="contact__person">
      <div class="contact__name">Tomas Wrenfield</div>
      <div class="contact__role">CEO</div>
    </div>
    <ul class="contact__list">
      <li>+ 62 817 402 36918
        <svg class="contact__icon" viewBox="0 0 14 14"><path d="M3 1l3 3-2 2c1 2 2 3 4 4l2-2 3 3-2 2C6 13 1 8 1 3z" fill="var(--white)"/></svg></li>
      <li>+ 65 9143 5820
        <svg class="contact__icon" viewBox="0 0 14 14"><rect x="3.5" y="1" width="7" height="12" rx="1" fill="var(--white)"/><rect x="5" y="3" width="4" height="6" fill="var(--orange)"/></svg></li>
      <li>+1 650 271 8845
        <svg class="contact__icon" viewBox="0 0 14 14"><path d="M3 1l3 3-2 2c1 2 2 3 4 4l2-2 3 3-2 2C6 13 1 8 1 3z" fill="var(--white)"/></svg></li>
      <li>tomas@veltopayments.example
        <svg class="contact__icon" viewBox="0 0 14 14"><rect x="1" y="3" width="12" height="8" fill="var(--white)"/><path d="M1 3l6 5 6-5" fill="none" stroke="var(--orange)" stroke-width="1.2"/></svg></li>
      <li class="is-strong">www.veltopayments.example
        <svg class="contact__icon" viewBox="0 0 14 14"><circle cx="7" cy="7" r="6" fill="var(--white)"/><path d="M1 7h12M7 1c-3 3-3 9 0 12M7 1c3 3 3 9 0 12" fill="none" stroke="var(--orange)" stroke-width="1"/></svg></li>
    </ul>
  </section>

  <section class="card card--brand" aria-label="Brand side">
    <svg class="card__art" viewBox="0 0 640 366" aria-hidden="true">
      <polygon points="380,0 640,0 640,366 560,366" fill="var(--orange)"/>
    </svg>
    <div class="brand__logo">KirbeX</div>
    <div class="brand__url">www.KirbeX.example</div>
    <div class="brand__social">
      <span><i></i>@KirbeX_id</span>
      <span><i></i>/KirbeX</span>
    </div>
  </section>

</main>
</body>
</html>
```